Innovative psychologist for companies seeks web design for website

Psychologist offers 2 topics:
1. What can a company do to ensure that employees are satisfied and enjoy their work?
The following explanatory video is linked on the website:
https://www.clipvarno.com/watch?v=qTrmWbLpoZd
2. How can you successfully change your own behavior?
Explanatory video: https://www.clipvarno.com/watch?v=HwkPZaGuoTb&t=6s
The slogan for the second theme will be: YOU are the pirate of your life!

Target Market(s)

companies and private individuals

Number of Pages Required

1 page

Requirements
Nice to have
• Characteristics of the psychologist: pragmatic, down-to-earth, honest, direct, appreciative, enjoys life, loves nature

```html
<!DOCTYPE html>
<html lang="en">
<head>
<meta charset="utf-8">
<title>Nora Velden – Work Happy</title>
<link href="https://fonts.googleapis.com/css2?family=Montserrat:wght@400;500;600;700&family=Lexend:wght@200&display=swap" rel="stylesheet">
<style>
  :root{
    --stage:#5f5f5f;
    --paper:#ffffff;
    --ink:#1d1d1d;
    --muted:#6d6d74;
    --brand-blue:#5b6bb6;
    --brand-pink:#e8699d;
    --navy:#1b2352;
    --footer:#1b1b1b;
    --soft-gray:#ececec;
  }
  *{box-sizing:border-box;margin:0;padding:0}
  html,body{width:1200px;height:1000px;overflow:hidden}
  body{background:var(--stage);font-family:"Montserrat",sans-serif;color:var(--ink);position:relative}
  .page{position:absolute;left:320px;top:9px;width:560px;height:982px;background:var(--paper);overflow:hidden}
  .abs{position:absolute}

  /* header */
  .site-header{left:0;top:0;width:560px;height:34px;border-bottom:1px solid #eee}
  .brand{left:36px;top:10px;display:flex;align-items:center;gap:4px;font-weight:700;font-size:10px;color:var(--ink);letter-spacing:.2px}
  .brand-dot{width:9px;height:9px;background:var(--brand-pink)}
  .nav{left:149px;top:13px;display:flex;align-items:center;font-size:6.5px;font-weight:700;letter-spacing:.2px}
  .nav a{color:var(--ink);text-decoration:none;position:relative}
  .nav a.active{color:var(--brand-blue)}
  .nav a.active::after{content:"";position:absolute;left:-1px;right:-1px;top:20px;height:2px;background:var(--brand-blue)}
  .nav .sep{margin:0 13px;font-weight:400}
  .help{left:450px;top:7px;display:flex;gap:5px;align-items:center}
  .help-text small{display:block;font-size:6px;color:var(--muted)}
  .help-text strong{display:block;font-size:8px;color:var(--brand-pink);font-weight:700;margin-top:1px}

  /* hero */
  .hero{left:0;top:34px;width:560px;height:284px}
  .hero-title{left:36px;top:104px;font-family:"Lexend",sans-serif;font-weight:200;font-size:33px;letter-spacing:.5px;color:var(--ink)}
  .hero-sub{left:36px;top:153px;width:200px;font-size:10.5px;line-height:15px;color:var(--ink)}
  .hero-sub b{color:var(--brand-blue);font-weight:600}
  .btn{display:flex;align-items:center;gap:6px;background:var(--brand-blue);color:#fff;font-size:5.5px;font-weight:600;border-radius:3px;letter-spacing:.2px}
  .hero-btn{left:36px;top:200px;width:71px;height:20px;padding-left:10px}

  /* characteristics */
  .traits-title{left:36px;top:349px;font-size:16.5px;line-height:20px;font-weight:500}
  .traits-title b{font-weight:700}
  .traits-intro{left:234px;top:354px;width:206px;font-size:5.6px;line-height:8.3px;color:var(--muted)}
  .traits-btn{left:464px;top:358px;width:71px;height:20px;padding-left:10px}
  .card{top:407px;width:158px;height:173px;border-radius:9px;overflow:hidden}
  .card-photo{position:absolute;inset:0}
  .card-label{position:absolute;left:22px;top:136px;color:#fff;font-size:8.5px;line-height:11.5px;font-weight:500}
  .card-icon{position:absolute;left:20px;top:102px}
  .card-note{position:absolute;left:11px;top:75px;width:136px;height:88px;background:#fff;border-radius:8px;padding:10px 8px 0 35px}
  .card-note h3{font-size:8px;line-height:10px;font-weight:600;color:var(--ink)}
  .card-note p{font-size:5.3px;line-height:8px;color:var(--muted);margin-top:4px;width:96px}
  .card-note svg{position:absolute;left:6px;top:9px}
  .slider-arrow{width:18px;height:18px;background:#fff;border-radius:3px;display:flex;align-items:center;justify-content:center}

  /* video band */
  .video-band{left:0;top:614px;width:560px;height:174px}
  .band-more{left:400px;top:737px;color:#fff;font-size:7px;font-weight:600;display:flex;gap:5px;align-items:center;letter-spacing:.3px}

  /* footer */
  .site-footer{left:0;top:788px;width:560px;height:194px;background:var(--footer);color:#fff}
  .f-h{font-size:10px;font-weight:700}
  .f-about p{font-size:5.8px;line-height:10.5px;width:118px;margin-bottom:9px}
  .f-links li{list-style:none;font-size:5.8px;margin-bottom:10.5px}
  .f-links li::before{content:"›";color:var(--brand-pink);margin-right:3px;font-weight:700}
  .social{display:flex;gap:6px}
  .social span{width:16px;height:16px;border-radius:50%;background:#fff;display:block}
  .copyright{font-size:6px}
  .f-brand{font-size:10px;font-weight:700;display:flex;align-items:center;gap:4px}
</style>
</head>
<body>
<div class="page">

  <header class="site-header abs">
    <div class="brand abs"><span class="brand-dot"></span>Nora Velden</div>
    <nav class="nav abs">
      <a class="active">HOME</a><span class="sep">|</span>
      <a>ABOUT</a><span class="sep">|</span>
      <a>CULTURE</a><span class="sep">|</span>
      <a>BENEFITS</a><span class="sep">|</span>
      <a>CONTACT</a>
    </nav>
    <div class="help abs">
      <svg width="16" height="16" viewBox="0 0 16 16" fill="none" stroke="var(--brand-blue)" stroke-width="1.3">
        <path d="M3 9V7a5 5 0 0 1 10 0v2"/><rect x="2" y="8.5" width="2.5" height="4" rx="1"/><rect x="11.5" y="8.5" width="2.5" height="4" rx="1"/><path d="M13 12.5c0 1.5-2 2-4 2"/>
      </svg>
      <div class="help-text"><small>Have Any Questions?</small><strong>044-987 654 321</strong></div>
    </div>
  </header>

  <section class="hero abs">
    <svg class="abs" style="left:0;top:0" width="560" height="284" viewBox="0 0 560 284">
      <polygon points="207,284 289,202 289,284" fill="var(--soft-gray)"/>
      <polygon points="289,72 365,0 480,0 289,186" fill="var(--brand-blue)"/>
      <defs>
        <linearGradient id="heroPhoto" x1="0" y1="0" x2="1" y2="1">
          <stop offset="0" stop-color="#c9c4bd"/>
          <stop offset=".5" stop-color="#8a6f5a"/>
          <stop offset="1" stop-color="#5b5f6e"/>
        </linearGradient>
      </defs>
      <polygon points="343,284 475,23 560,23 560,284" fill="url(#heroPhoto)" role="img" aria-label="Photo of two smiling colleagues celebrating at a desk"/>
      <line x1="325" y1="290" x2="500" y2="60" stroke="#fff" stroke-width="5"/>
    </svg>
    <h1 class="hero-title abs">WORK HAPPY</h1>
    <p class="hero-sub abs">Transforming the workplace into a playground of <b>joy</b> and <b>creativity!</b></p>
    <a class="btn hero-btn abs">JOIN THE FUN
      <svg width="9" height="6" viewBox="0 0 9 6" fill="none" stroke="#fff" stroke-width="1"><path d="M0 3h8M5.5 .5 8 3 5.5 5.5"/></svg></a>
  </section>

  <h2 class="traits-title abs">Characteristics<br>of the <b>Psychologist</b></h2>
  <p class="traits-intro abs">Lorem Ipsum is simply dummy text of the printing and typesetting industry. Lorem Ipsum has been the industry's standard dummy text ever since the 1500s, when an unknown printer took a galley of type and scrambled.</p>
  <a class="btn traits-btn abs">READ MORE
    <svg width="9" height="6" viewBox="0 0 9 6" fill="none" stroke="#fff" stroke-width="1"><path d="M0 3h8M5.5 .5 8 3 5.5 5.5"/></svg></a>

  <article class="card abs" style="left:37px">
    <div class="card-photo" role="img" aria-label="Photo of an office worker with a headset at her desk" style="background:linear-gradient(180deg,#b7c4cf 0%,#7c8ea0 45%,#1b2352 85%)"></div>
    <svg class="card-icon" width="22" height="26" viewBox="0 0 22 26" fill="none" stroke="#fff" stroke-width="1.3"><path d="M4 25v-6C1 17 1 12 3 8a9 9 0 0 1 16 3l2 5h-3v4h-4v5"/><circle cx="11" cy="10" r="3"/></svg>
    <p class="card-label">Pragmatic Thinking,<br>Practical Solutions!</p>
  </article>

  <article class="card abs" style="left:207px">
    <div class="card-photo" role="img" aria-label="Photo of two colleagues reviewing work together" style="background:linear-gradient(180deg,#d8d6d2 0%,#9aa0ab 45%,#1b2352 90%)"></div>
    <div class="card-note">
      <svg width="24" height="22" viewBox="0 0 24 22" fill="none" stroke="var(--ink)" stroke-width="1.3"><path d="M1 8l5-5 4 2 4-2 5 2 4 4-9 9-4-3-3 1-6-8z"/><path d="M10 5l-3 4 2 1 4-3"/></svg>
      <h3>Stay Grounded,<br>Live Down to Earth!</h3>
      <p>Lorem Ipsum is simply dummy text of the printing and typesetting industry. Lorem Ipsum has been the industry's standard dummy text ever since the 1500s.</p>
    </div>
  </article>

  <article class="card abs" style="left:377px">
    <div class="card-photo" role="img" aria-label="Photo of two businessmen reading a document" style="background:linear-gradient(180deg,#c7c2b8 0%,#6d6f78 45%,#1b2352 85%)"></div>
    <svg class="card-icon" width="22" height="28" viewBox="0 0 22 28" fill="none" stroke="#fff" stroke-width="1.3"><circle cx="9" cy="5" r="3"/><path d="M4 27V14a5 5 0 0 1 10 0v13M14 14l6-8"/></svg>
    <p class="card-label">Honesty: The Foundation of<br>Trust and Integrity.</p>
  </article>

  <span class="slider-arrow abs" style="left:44px;top:482px">
    <svg width="8" height="6" viewBox="0 0 8 6" fill="none" stroke="var(--ink)" stroke-width="1"><path d="M8 3H1M3.5 .5 1 3l2.5 2.5"/></svg></span>
  <span class="slider-arrow abs" style="left:509px;top:482px">
    <svg width="8" height="6" viewBox="0 0 8 6" fill="none" stroke="var(--ink)" stroke-width="1"><path d="M0 3h7M4.5 .5 7 3 4.5 5.5"/></svg></span>

  <section class="video-band abs">
    <svg width="560" height="174" viewBox="0 0 560 174">
      <defs>
        <linearGradient id="crowd" x1="0" y1="0" x2="0" y2="1">
          <stop offset="0" stop-color="#8a8170"/><stop offset=".55" stop-color="#3e3630"/><stop offset="1" stop-color="#5b5148"/>
        </linearGradient>
        <linearGradient id="office" x1="0" y1="0" x2="1" y2="0">
          <stop offset="0" stop-color="#4e5c9e"/><stop offset="1" stop-color="#8b97c6"/>
        </linearGradient>
      </defs>
      <rect x="0" y="0" width="300" height="174" fill="url(#crowd)" role="img" aria-label="Video still of friends dancing outdoors at sunset"/>
      <rect x="290" y="0" width="270" height="174" fill="url(#office)" role="img" aria-label="Photo of a bright office, tinted blue"/>
      <polygon points="250,0 310,0 380,87 310,174 250,174 320,87" fill="var(--brand-pink)" opacity=".92"/>
      <polygon points="355,87 485,87 525,174 380,174" fill="var(--brand-blue)"/>
      <circle cx="135" cy="87" r="17" fill="#fff" opacity=".85"/>
      <polygon points="130,78 130,96 144,87" fill="#222"/>
    </svg>
  </section>
  <a class="band-more abs">READ MORE
    <svg width="9" height="6" viewBox="0 0 9 6" fill="none" stroke="#fff" stroke-width="1"><path d="M0 3h8M5.5 .5 8 3 5.5 5.5"/></svg></a>

  <footer class="site-footer abs">
    <h4 class="f-h abs" style="left:36px;top:28px">About Us</h4>
    <div class="f-about abs" style="left:36px;top:58px">
      <p>Lorem Ipsum is simply dummy text of the printing and typesetting industry. Lorem Ipsum has been.</p>
      <p>The industry's standard dummy text ever since the 1500s, when an unknown printer too.</p>
    </div>
    <h4 class="f-h abs" style="left:257px;top:28px">Quick Links</h4>
    <ul class="f-links abs" style="left:257px;top:60px">
      <li>Home</li><li>About</li><li>Culture</li><li>Benefits</li><li>Contact</li>
    </ul>
    <h4 class="f-h abs" style="left:442px;top:28px">Follow Us</h4>
    <div class="social abs" style="left:442px;top:61px"><span></span><span></span><span></span></div>
    <p class="copyright abs" style="left:36px;top:177px">Copyright © 2024 web site name. All rights reserved.</p>
    <div class="f-brand abs" style="left:452px;top:174px"><span class="brand-dot"></span>Nora Velden</div>
  </footer>

</div>
</body>
</html>
```